Cybersecurity company is looking for business card.

I need a business card design for our company, we are a cybersecurity company providing advance technology to protect agains any kind of malware. We need a fresh modern design it should communicate modern, technology and growth.

Target Market(s)

Business to business

Industry/Entity Type

Business

Contact Information for Business Card

Should have location, address, fax, mobile, phone, email and website.

Requirements
Must have
• Must follow company's logo color and style. Must have the company's log on its.

```html
<!DOCTYPE html>
<html lang="en">
<head>
<meta charset="utf-8">
<title>Cyvarta Business Card</title>
<link rel="stylesheet" href="https://fonts.googleapis.com/css2?family=Michroma&family=Tenor+Sans&display=swap">
<style>
  :root {
    --bg: #34434c;
    --brand-red: #9e1b20;
    --ink: #141414;
    --ink-soft: #333333;
    --paper: #ffffff;
    --rule: #c8c8c8;
    --logo-light: #e4e4e4;
  }
  * { box-sizing: border-box; margin: 0; padding: 0; }
  html, body { width: 1200px; height: 1000px; overflow: hidden; }
  body {
    background: var(--bg);
    font-family: "Tenor Sans", sans-serif;
    position: relative;
  }
  .card {
    position: absolute;
    left: 240px;
    width: 720px;
    height: 412px;
    box-shadow: 0 10px 28px rgba(0,0,0,.35);
  }
  .card--front {
    top: 52px;
    background: var(--brand-red);
    display: flex;
    align-items: center;
    justify-content: center;
  }
  .card--back {
    top: 530px;
    background: var(--paper);
  }
  .wordmark {
    font-family: "Michroma", sans-serif;
    font-weight: 400;
    letter-spacing: 1px;
    line-height: 1;
  }
  .card--front .wordmark {
    font-size: 72px;
    color: var(--logo-light);
  }
  .identity {
    position: absolute;
    top: 58px;
    right: 450px;
    text-align: right;
  }
  .identity__name {
    font-family: "Michroma", sans-serif;
    font-size: 17px;
    color: var(--ink);
    letter-spacing: .5px;
  }
  .identity__title {
    font-size: 14px;
    color: var(--ink-soft);
    margin-top: 8px;
  }
  .divider {
    position: absolute;
    left: 288px;
    top: 48px;
    width: 1px;
    height: 96px;
    background: var(--rule);
  }
  .card--back .wordmark {
    position: absolute;
    left: 312px;
    top: 66px;
    font-size: 40px;
    color: var(--ink);
  }
  .contacts {
    position: absolute;
    left: 300px;
    top: 186px;
    list-style: none;
  }
  .contacts li {
    display: flex;
    align-items: center;
    height: 34px;
    font-size: 17px;
    color: var(--ink);
    letter-spacing: .5px;
  }
  .contacts svg {
    width: 22px;
    height: 22px;
    margin-right: 12px;
    flex: none;
  }
  .address {
    position: absolute;
    right: 470px;
    bottom: 42px;
    text-align: right;
    font-style: italic;
    font-size: 16px;
    line-height: 1.55;
    color: var(--ink);
  }
</style>
</head>
<body>
  <section class="card card--front">
    <span class="wordmark">cyvarta</span>
  </section>

  <section class="card card--back">
    <div class="identity">
      <p class="identity__name">Name Here</p>
      <p class="identity__title">Position / Title</p>
    </div>
    <div class="divider"></div>
    <span class="wordmark">cyvarta</span>

    <ul class="contacts">
      <li>
        <svg viewBox="0 0 22 22"><circle cx="11" cy="11" r="11" fill="#9e1b20"/><rect x="7.5" y="5" width="7" height="12" rx="1.2" fill="#fff"/><rect x="8.7" y="6.5" width="4.6" height="8" fill="#9e1b20"/></svg>
        +971 52 123 XXXX
      </li>
      <li>
        <svg viewBox="0 0 22 22"><circle cx="11" cy="11" r="11" fill="#9e1b20"/><path d="M7 5.5l2.2-.3 1.2 3-1.4 1.1c.7 1.5 1.9 2.7 3.4 3.4l1.1-1.4 3 1.2-.3 2.2c-5 .4-9.6-4.2-9.2-9.2z" fill="#fff"/></svg>
        04 123 XXXX
      </li>
      <li>
        <svg viewBox="0 0 22 22"><circle cx="11" cy="11" r="11" fill="#9e1b20"/><rect x="6" y="9" width="10" height="7" rx="1" fill="#fff"/><rect x="8" y="5.5" width="6" height="4" fill="#fff"/><rect x="8.5" y="11" width="5" height="1.2" fill="#9e1b20"/><rect x="8.5" y="13" width="5" height="1.2" fill="#9e1b20"/></svg>
        04 123 XXXX
      </li>
      <li>
        <svg viewBox="0 0 22 22"><circle cx="11" cy="11" r="11" fill="#9e1b20"/><rect x="5.5" y="7" width="11" height="8" rx="1" fill="#fff"/><path d="M5.8 7.4L11 11.4l5.2-4" stroke="#9e1b20" stroke-width="1.2" fill="none"/></svg>
        name.surname@cyvarta.com
      </li>
      <li>
        <svg viewBox="0 0 22 22"><circle cx="11" cy="11" r="11" fill="#9e1b20"/><g fill="none" stroke="#fff" stroke-width="1.8"><rect x="5.5" y="10" width="6" height="4" rx="2" transform="rotate(-45 8.5 12)"/><rect x="10.5" y="8" width="6" height="4" rx="2" transform="rotate(-45 13.5 10)"/></g></svg>
        www.cyvarta.com
      </li>
    </ul>

    <address class="address">
      Harbor Tech Park (HTP),<br>
      Marina Boulevard,<br>
      Dubai - UAE
    </address>
  </section>
</body>
</html>
```